Mobile Repair Service on location needs a Web Design

We are starting a new mobile device repair service called Gadget Haven and our website needs a design!

Hello Designers!
First, we'd like to make clear this is more than a simple web design contest, we want the designers to create an idea. We want someone who can create the whole theme of the service's we provide. We want someone that can help design our visual branding, help us communicate a sentiment. And we are willing to pay for that.

Who are we?
Our company is based in Rotterdam, the Netherlands. We provide different services for all kinds of electronic devices. The kind of services we provide are, among other things, installations of hardware and software and the repair of broken or malfunctioning devices.
We are starting a new service that offers mobile device repairs on location, be it at the home of our customers, their office, or any other place. Just give us the address and we will come to you for the repair job. This is also our main USP. We have multiple skilled engineers who drive trough the country on a daily basis and can be on location within a working day. Repair is done immediately onsite while the customer waits. At this stage we will start with the smartphone product-group within the mobile devices. In a second phase we might also add tablets.
People don't want to be without their phone for weeks because of some parts that needed to be ordered by a repair center they had to sent their phone to. We offer a fully functional mobile repair center in the form of specially customized vans. These vans have all the tools and utilities needed by our engineers to safely repair your mobile device. Your phone is being repaired directly in front of you, the next business-day, on a location you desire.

For this new service we are creating a website called Gadget Haven. The website needs a story and matching design and this is where you come in. We are not looking for a simple template design we can get from any place. We need a story. We want you to create an idea, build a unique theme or vision that helps sell the product/service. This goes beyond the design of the website. We need the whole package, the design you are creating needs to have returning elements like icons, color use, images, maybe even characters etc. You name it! There needs to be a common thread in the design so we can reuse elements in, for example, the email templates, the work order or receipt we give to our customers (we may contact the winner of the contest to design these for us as well!).

The name 'Gadget Haven' is chosen. Haven (short for rehabilitate) has a bold and playful tone to it and the design needs to reflect the name. So we're looking for a somewhat playful and cheeky design. Definitely not too serious and definitely modern. We already got a logo that we love and that fit's this description (see attached design documents for the logo). It's bold, powerful and fun. Our web design needs to reflect this as well and has to fit in with our logo.
We would really like it if the design somehow incorporates elements that highlight our unique selling points (repairs on location, we come to you etc.). We would really like some form of story telling in the design. Think clumsy people breaking their phones. Teenagers in tears because they have no access to their friends. People nowadays have the need to always be 'connected'. What happens when your phone is broken or malfunctioning? We're handling tech, we are nerds and a little bit weird, but we're professionals and here to help you with your problem. The sentiment Wire Troop tries to communicate is something we really like. We're looking for fresh idea's, anything goes!

In an overview all Unique Selling Points of the Gadget haven service:
- Professional service on location. Don’t ship to us we will come to you!
- Clear pricing upfront. No hidden cost.
- Next business-day repair.
- Backed by a professional call center open 12 hours a day and open on a Saturday as well
- Backed by a professional repair center with more then 12 years of experience
- Repair is done by certified engineers
- 1 year warranty on the repair

The process:
The main function of our website will be for customers to make a repair request. A customer will visit our website and can make a repair request immediately by going through a 'request-order-flow'. In this flow he or she will need to fill in some forms and can select wich type/model/brand of mobile device he or she has and what parts need to be repaired. After a request is placed we will call the customer back (within an hour) for a short intake and to set a date/time and location. Our engineer will meet the customer at the specified location and will repair the device onsite in one of our mobile repair centers, which is a specialized van equipped with all the tools needed for device restorations.
So in short the steps are:
- Choose your device and repair job
- Place the order
- Get a callback within the hour
- Set date and location
- We will come to you.

Website functionality:
Our website is our main form of communication. So the sentiment we want to communicate needs be reflected in the design. We need a main/front page designed (preferably a long scrolling page design) containing:
1. Customers will be able to request a repair job directly on our website. So there will need to be a prominent button/link at the top of our main page that will bring the customer to this 'request-order-flow'. This is the main flow which needs to be full focus on the front page. All other items are secondary.
2. The general information of who we are and what we do, and why the customer should choose us. Preferably in short bullet-point type keywords/sentences with icons or other visual cues. See our unique selling points to get an idea of the information that will be displayed here.
3. There needs to be a section that will explain the process (see above) of a repair request step-by- step, again in brief short key sentences and with (custom) icons.
4. There needs to be a section that explains to the customer he/she can always contact us if they are not sure what the problem is with their device, and for this reason are not sure what repair request they should order.
5. We want to implement some functionality that display customer ratings or customer reviews. So there needs to be room for some kind of widget of plugin we're going to implement which shows these reviews.
6. A 'For business section' where we will explain all the options we provide for corporate clients.
7. Social media links.
8. There needs to be a menu with buttons that leads to the all sections described in the previous points.

For now, we need a design for our front page. In the second phase, when we have picked our winner, we may ask the winner to design the page(s) for our request workflow as well.

EDIT:
Finally, we have a very specific order in mind for the different segments of our website. We would like you to add some more segments that were not in our original brief as well:

1. Top header with order/request button. (should instantly make clear our main USP, we do repairs on location)
2. Our process
3. Our unique selling points / why choose us
4. The kind of repairs we do (broken screens, broken batteries, water damage, broken camera's, no sound etc.)
5. A 'meet our team' section, where we introduce some of our engineers
6. A 'contact us for any questions' section/
7. Testimonials/user reviews
8. A section where we show key performance indicators
9. 'For businesses' sections
10.'Subscribe for newsletter' field
11. Social media buttons

Industry/Entity Type

It Service

Number of Pages Required

1 page

Font styles to use
Sans Serif

Requirements
Must have
• a main/front page, design only
• custom icons/images for banners, adverts online and in print (high res)
Nice to have
• Storytelling in our design.
• Design that fits with our brand new logo.
• Elements like icons to have a flat design.
• Keep in mind that the website will need to be responsive when designing! (Ideally provide an example of the mobile design as well)
• Create a fun and trustworthy feeling.

```html
<!DOCTYPE html>
<html lang="en">
<head>
<meta charset="utf-8">
<title>Gadget Haven – Mobile repair on location</title>
<link rel="stylesheet" href="https://fonts.googleapis.com/css2?family=Roboto:wght@300;400;500;700&display=swap">
<style>
:root{
  --orange:#e8601c;
  --orange-dark:#c94e12;
  --ink:#2b2b2b;
  --charcoal:#28292d;
  --charcoal-2:#323337;
  --grey-card:#545454;
  --light:#f3f3f3;
  --muted:#8a8a8a;
  --white:#ffffff;
}
*{box-sizing:border-box;margin:0;padding:0}
html,body{width:1200px;height:3077px;overflow:hidden}
body{position:relative;font-family:"Roboto",Arial,sans-serif;color:var(--ink);background:var(--white)}
.abs{position:absolute}
section,header,footer{position:absolute;left:0;width:1200px}

/* Header */
.site-header{top:0;height:96px;background:var(--white)}
.brand{left:92px;top:16px;display:flex;align-items:center;gap:10px}
.brand-mark{width:52px;height:52px;border-radius:50%;background:var(--orange)}
.brand-name{font-weight:700;font-size:22px;line-height:22px;color:var(--ink);width:100px}
.brand-tag{font-size:9px;color:var(--muted);margin-top:3px;font-weight:400}
.top-phone{right:56px;top:6px;font-size:17px;color:var(--ink)}
.main-nav{left:410px;top:50px;display:flex;gap:0;font-size:14px;color:#555}
.main-nav a{color:#555;text-decoration:none;position:absolute;white-space:nowrap}
.btn-track{left:970px;top:41px;width:144px;height:37px;background:var(--orange);color:var(--white);font-size:15px;display:flex;align-items:center;justify-content:center}

/* Hero */
.hero{top:96px;height:464px;background:linear-gradient(100deg,#121212 0%,#1d1d1f 45%,#3a3a3c 70%,#27344a 88%,#1a1a1c 100%)}
.hero-photo{right:0;top:0;width:560px;height:464px;background:radial-gradient(ellipse at 70% 45%,rgba(210,200,190,.35),rgba(20,20,20,0) 65%)}
.hero h1{left:142px;top:104px;font-size:55px;font-weight:400;color:var(--white)}
.hero-feature{display:flex;align-items:center;gap:14px;color:var(--white);font-size:19px;font-weight:300}
.hero-feature svg{width:30px;height:30px}
.btn{height:47px;display:flex;align-items:center;justify-content:center;font-size:18px;font-weight:500;border-radius:2px}
.btn-get{left:148px;top:304px;width:227px;background:var(--orange);color:var(--white);border-right:14px solid var(--orange-dark)}
.btn-call{left:402px;top:304px;width:221px;background:var(--white);color:var(--ink);border-right:14px solid var(--orange);gap:8px}

/* How it works */
.how{top:560px;height:363px;background:linear-gradient(#f6f6f6,#fbfbfb)}
.section-title{width:100%;text-align:center;font-size:28px;font-weight:400;color:var(--ink)}
.section-title .q{color:var(--orange)}
.step{top:133px;width:221px;height:169px;background:var(--white);border-radius:8px;box-shadow:0 2px 6px rgba(0,0,0,.12);overflow:hidden}
.step-num{top:-12px;width:28px;height:28px;border-radius:50%;background:var(--orange);color:var(--white);font-size:14px;display:flex;align-items:center;justify-content:center;transform:translateX(-50%)}
.step-icon{left:72px;top:38px;width:78px;height:74px;border-radius:6px;background:linear-gradient(#f0f0f0,#e4e4e4)}
.step-label{left:0;bottom:0;width:100%;height:42px;background:#3a3a3a;color:var(--white);font-size:15px;display:flex;align-items:center;justify-content:center}
.step-label.is-last{background:var(--orange)}

/* Who are we */
.about{top:923px;height:427px;background:var(--white)}
.about-photo{left:0;top:0;width:732px;height:427px;background:linear-gradient(90deg,rgba(20,20,20,.95) 0%,rgba(35,35,35,.9) 55%,#4a4440 100%)}
.about h2{left:84px;top:68px;font-size:26px;font-weight:400;color:var(--white)}
.about h2 .q{color:var(--orange)}
.about p{left:84px;top:117px;width:420px;font-size:15.5px;line-height:26px;color:#ddd;font-weight:300}
.btn-more{left:84px;top:283px;width:164px;height:45px;background:var(--white);color:var(--ink);font-size:16px;border-right:12px solid var(--orange);border-left:4px solid var(--orange)}
.about-ring{left:706px;top:24px;width:380px;height:380px;border-radius:50%;border:26px solid var(--orange);background:#f1f1f1}
.about-device{left:778px;top:0;width:228px;height:434px;border-radius:40px;background:linear-gradient(#f4f4f4,#dcdcdc);box-shadow:0 2px 8px rgba(0,0,0,.2)}

/* Testimonials */
.reviews{top:1350px;height:472px;background:var(--white)}
.reviews-photo{left:0;top:14px;width:370px;height:458px;background:linear-gradient(160deg,#f4f4f4 0%,#e9d8cc 45%,#e2622a 80%,#f2f2f2 100%)}
.reviews h2{left:370px;top:100px;width:728px;text-align:center;font-size:24px;font-weight:500;color:var(--ink)}
.review{width:193px;height:166px;background:var(--grey-card);color:var(--white);text-align:center;padding:78px 14px 0}
.review.is-featured{background:var(--orange);height:199px;padding-top:88px;width:228px}
.review .avatar{left:50%;top:20px;width:50px;height:50px;border-radius:50%;background:#bbb;transform:translateX(-50%);border:2px solid var(--white)}
.review.is-featured .avatar{top:28px}
.review .quote{right:12px;top:10px;font-size:26px;font-weight:700;line-height:26px}
.review h3{font-size:14px;font-weight:400;margin-bottom:4px}
.review p{font-size:11.5px;line-height:15px;font-weight:300}
.carousel-arrow{font-size:22px;color:var(--ink)}
.dots{left:716px;top:1389px;display:flex;gap:8px}
.dot{width:8px;height:8px;border-radius:50%;background:#555}
.dot.is-active{background:var(--orange)}

/* Brands */
.brands{top:1822px;height:410px;background:var(--charcoal)}
.brands h2{top:40px;width:100%;text-align:center;font-size:24px;font-weight:500;color:var(--orange)}
.brands .sub{top:76px;width:100%;text-align:center;font-size:14px;color:#ccc;font-weight:300}
.brand-grid{left:92px;top:128px;width:996px;display:grid;grid-template-columns:repeat(6,166px);grid-template-rows:repeat(2,132px)}
.brand-cell{display:flex;align-items:center;justify-content:center;font-size:22px;font-weight:500;letter-spacing:2px;color:#8d8d8f;text-transform:uppercase;border-right:1px solid rgba(255,255,255,.05);border-bottom:1px solid rgba(255,255,255,.05)}
.brand-cell:nth-child(6n){border-right:none}
.brand-cell:nth-child(n+7){border-bottom:none}

/* Stats */
.stats{top:2232px;height:393px;background:var(--white)}
.stats-photo{left:0;top:0;width:1200px;height:240px;background:linear-gradient(180deg,#151515,#2b2a2a 55%,#4a4644 100%)}
.stat{top:112px;width:222px;height:168px;border-radius:8px;overflow:hidden;border:1px solid rgba(255,255,255,.4)}
.stat-value{height:132px;background:rgba(40,40,40,.75);color:var(--white);font-size:38px;font-weight:700;display:flex;align-items:center;justify-content:center;padding-top:30px}
.stat-label{height:36px;background:var(--orange);color:var(--white);font-size:15px;display:flex;align-items:center;justify-content:center}

/* Footer */
.site-footer{top:2625px;height:452px;background:var(--charcoal-2)}
.contact-panel{left:88px;top:0;width:431px;height:386px;background:var(--orange)}
.contact-panel h2{top:32px;width:100%;text-align:center;font-size:30px;font-weight:400;color:var(--white)}
.field{left:10px;width:407px;height:35px;background:#eeeeee;font-size:11px;color:#999;padding:8px 8px}
.btn-send{left:10px;top:314px;width:115px;height:41px;background:#444;color:var(--white);font-size:15px;display:flex;align-items:center;justify-content:center;gap:14px}
.footer-col h3{font-size:17px;font-weight:500;color:var(--white);margin-bottom:16px}
.footer-col p,.footer-col li{font-size:12px;color:#ddd;line-height:21px;font-weight:300}
.footer-col ul{list-style:none}
.footer-col li{display:flex;align-items:center;gap:12px;margin-bottom:8px}
.newsletter{display:flex;margin-bottom:10px}
.newsletter .input{width:172px;height:33px;background:var(--white);font-size:10px;color:#999;padding:10px 8px}
.newsletter .go{width:41px;height:33px;background:var(--orange);display:flex;align-items:center;justify-content:center}
.bottom-bar{left:0;top:386px;width:1200px;height:66px;background:var(--charcoal)}
.legal-links{left:113px;top:26px;display:flex;gap:10px;font-size:10px;color:#ccc;letter-spacing:1px}
.social{left:532px;top:20px;display:flex;gap:17px}
.social span{width:24px;height:24px;border-radius:50%;background:#d8d8d8}
.copyright{right:99px;top:26px;font-size:11px;color:#ccc}
</style>
</head>
<body>

<header class="site-header">
  <div class="abs brand">
    <span class="brand-mark"></span>
    <div><div class="brand-name">GADGET HAVEN</div><div class="brand-tag">We will come to you!</div></div>
  </div>
  <div class="abs top-phone">+987 555 0142</div>
  <nav class="abs main-nav" style="left:0;top:50px">
    <a style="left:410px">Repair</a>
    <a style="left:480px">Shop</a>
    <a style="left:543px">Support</a>
    <a style="left:625px">How It Works</a>
    <a style="left:740px">Knowledge Centre</a>
    <a style="left:886px">Customise</a>
  </nav>
  <div class="abs btn-track">Track My Order</div>
</header>

<section class="hero">
  <div class="abs hero-photo" role="img" aria-label="Photo of a technician's hands repairing a smartphone with a screwdriver"></div>
  <h1 class="abs">Get your Mobile repaired</h1>
  <div class="abs hero-feature" style="left:146px;top:180px">
    <svg viewBox="0 0 30 30" fill="none" stroke="#fff" stroke-width="2"><path d="M4 14h5v12H4zM9 24h12l4-9h-8l1-6-3-3-6 8"/></svg>3 Month Warranty</div>
  <div class="abs hero-feature" style="left:418px;top:180px">
    <svg viewBox="0 0 30 30" fill="none" stroke="#fff" stroke-width="2"><rect x="8" y="3" width="14" height="24" rx="2"/><path d="M13 23h4"/></svg>Stand-by Mobile</div>
  <div class="abs hero-feature" style="left:146px;top:222px">
    <svg viewBox="0 0 30 30" fill="none" stroke="#fff" stroke-width="2"><circle cx="9" cy="7" r="3"/><path d="M9 11v14M4 16h12l3-3"/><rect x="19" y="12" width="8" height="8"/></svg>Free Pick-up &amp; Drop</div>
  <div class="abs hero-feature" style="left:418px;top:222px">
    <svg viewBox="0 0 30 30" fill="none" stroke="#fff" stroke-width="2"><circle cx="15" cy="15" r="11"/><path d="M11 11h8M11 15h8M13 11c4 0 4 4 0 4l5 6"/></svg>Transparent Pricing</div>
  <div class="abs btn btn-get">GET REPAIRED</div>
  <div class="abs btn btn-call">
    <svg width="16" height="16" viewBox="0 0 24 24"><path fill="#2b2b2b" d="M6.6 10.8a15 15 0 006.6 6.6l2.2-2.2c.3-.3.7-.4 1-.2 1.1.4 2.3.6 3.6.6.6 0 1 .4 1 1V20c0 .6-.4 1-1 1A17 17 0 013 4c0-.6.4-1 1-1h3.5c.6 0 1 .4 1 1 0 1.3.2 2.5.6 3.6.1.3 0 .7-.2 1z"/></svg>
    +987 555 0142</div>
</section>

<section class="how">
  <h2 class="abs section-title" style="top:46px">How it works<span class="q">?</span></h2>
  <div class="abs step" style="left:105px"><div class="abs step-icon" role="img" aria-label="Icon: online order form"></div><div class="abs step-label">Generate Online Order</div></div>
  <div class="abs step" style="left:359px"><div class="abs step-icon" role="img" aria-label="Icon: courier handing over a parcel"></div><div class="abs step-label">Free Pick-up</div></div>
  <div class="abs step" style="left:611px"><div class="abs step-icon" role="img" aria-label="Icon: phone being repaired in a workshop"></div><div class="abs step-label">Diagnosis &amp; Repair</div></div>
  <div class="abs step" style="left:863px"><div class="abs step-icon" role="img" aria-label="Icon: phone returned with payment"></div><div class="abs step-label is-last">Receive Mobile &amp; Pay Cash</div></div>
  <div class="abs step-num" style="left:215px;top:121px">1</div>
  <div class="abs step-num" style="left:469px;top:121px">2</div>
  <div class="abs step-num" style="left:722px;top:121px">3</div>
  <div class="abs step-num" style="left:974px;top:121px">4</div>
</section>

<section class="about">
  <div class="abs about-photo" role="img" aria-label="Dark photo of an opened smartphone on a workbench"></div>
  <h2 class="abs">Who are we<span class="q">?</span></h2>
  <p class="abs">Our company is based in Rotterdam, the Netherlands. We provide different services for all kinds of electronic devices. The kind of services we provide are, among other things, installations of hardware and software and the repair of broken or malfunctioning devices.</p>
  <div class="abs btn btn-more">LEARN MORE</div>
  <div class="abs about-ring"></div>
  <div class="abs about-device" role="img" aria-label="Illustration of a smartphone showing the Gadget Haven app screen"></div>
</section>

<section class="reviews">
  <div class="abs reviews-photo" role="img" aria-label="Photo of a smiling customer on the phone giving a thumbs up"></div>
  <h2 class="abs">WHAT OUR CLIENTS SAY</h2>
  <div class="abs carousel-arrow" style="left:382px;top:256px">&#8249;</div>
  <div class="abs carousel-arrow" style="left:1077px;top:256px">&#8250;</div>
  <div class="abs review" style="left:414px;top:186px"><span class="abs avatar"></span><span class="abs quote">&rdquo;</span><h3>Lena Hart</h3><p>Nunc at diam a lorem faucibus placerat sed sed magna.</p></div>
  <div class="abs review is-featured" style="left:619px;top:170px"><span class="abs avatar"></span><span class="abs quote">&rdquo;</span><h3>Owen Price</h3><p>Nunc at diam a lorem faucibus placerat sed sed magna.</p></div>
  <div class="abs review" style="left:861px;top:186px"><span class="abs avatar"></span><span class="abs quote">&rdquo;</span><h3>Marco Vale</h3><p>Nunc at diam a lorem faucibus placerat sed sed magna.</p></div>
  <div class="abs dots" style="top:389px"><span class="dot is-active"></span><span class="dot"></span><span class="dot"></span></div>
</section>

<section class="brands">
  <h2 class="abs">BRANDS WE REPAIR</h2>
  <p class="abs sub">We repair almost any brands for mobiles and tablets</p>
  <div class="abs brand-grid">
    <div class="brand-cell">Sorvana</div><div class="brand-cell">Norbek</div><div class="brand-cell">Pomel</div>
    <div class="brand-cell">Hexo</div><div class="brand-cell">Levara</div><div class="brand-cell">Mikrova</div>
    <div class="brand-cell">Xandor</div><div class="brand-cell">Gilmo</div><div class="brand-cell">Intora</div>
    <div class="brand-cell">Karvel</div><div class="brand-cell">Zolta</div><div class="brand-cell">Lumo</div>
  </div>
</section>

<section class="stats">
  <div class="abs stats-photo" role="img" aria-label="Photo of smartphones and tools on a repair desk"></div>
  <div class="abs stat" style="left:224px"><div class="stat-value">100,000+</div><div class="stat-label">Smartphone Repaired</div></div>
  <div class="abs stat" style="left:478px"><div class="stat-value">97.7%</div><div class="stat-label">CSAT</div></div>
  <div class="abs stat" style="left:730px"><div class="stat-value">80,000+</div><div class="stat-label">Satisfied Customers</div></div>
</section>

<footer class="site-footer">
  <div class="abs contact-panel">
    <h2 class="abs">Get in touch</h2>
    <div class="abs field" style="top:76px">Name</div>
    <div class="abs field" style="top:121px">Email</div>
    <div class="abs field" style="top:164px">Phone</div>
    <div class="abs field" style="top:209px;height:95px">Message</div>
    <div class="abs btn-send">Send
      <svg width="14" height="14" viewBox="0 0 14 14" stroke="#fff" stroke-width="2"><path d="M2 2l10 10M12 2L2 12"/></svg></div>
  </div>
  <div class="abs footer-col" style="left:597px;top:114px;width:200px">
    <h3>Get In Touch</h3>
    <p style="margin-bottom:14px">123 Fusce non ipsum gravida, tempor ex a, sodales massa.</p>
    <ul>
      <li><svg width="12" height="12" viewBox="0 0 24 24"><path fill="#fff" d="M6.6 10.8a15 15 0 006.6 6.6l2.2-2.2c.3-.3.7-.4 1-.2 1.1.4 2.3.6 3.6.6.6 0 1 .4 1 1V20c0 .6-.4 1-1 1A17 17 0 013 4c0-.6.4-1 1-1h3.5c.6 0 1 .4 1 1 0 1.3.2 2.5.6 3.6.1.3 0 .7-.2 1z"/></svg>+44 (0)100 555012</li>
      <li><svg width="12" height="12" viewBox="0 0 12 12"><rect x="1" y="4" width="10" height="7" fill="#fff"/><rect x="3" y="1" width="6" height="3" fill="#fff"/></svg>+44 (0)100 555012</li>
      <li><svg width="12" height="12" viewBox="0 0 12 12"><rect x="1" y="2" width="10" height="8" fill="#fff"/><path d="M1 2l5 4 5-4" stroke="#333" fill="none"/></svg>sales@gadgethaven.com</li>
    </ul>
  </div>
  <div class="abs footer-col" style="left:845px;top:114px;width:260px">
    <h3>Gadget Haven &nbsp;in your inbox</h3>
    <div class="newsletter"><div class="input">Email Address</div><div class="go"><svg width="16" height="16" viewBox="0 0 16 16"><path fill="#fff" d="M15 1L1 7l5 2 2 6z"/></svg></div></div>
    <p>By signing up, you agree to our terms.</p>
  </div>
  <div class="abs bottom-bar">
    <div class="abs legal-links"><span>ABOUT</span><span>CONTACT</span><span>POLICY</span><span>ONLINEPAYMENT</span></div>
    <div class="abs social" aria-label="Social media links"><span></span><span></span><span></span><span></span></div>
    <div class="abs copyright">&copy; Copyright 2017 Gadget Haven</div>
  </div>
</footer>

</body>
</html>
```